Lumbrix Ventures Logo+Website+Social media design

We need a website/logo/social media design (LinkedIn, Facebook, Instagram, TikTok) for our 2 years-old company: Lumbrix Ventures. It's the company I've created to leave as a legacy for my sons, Lumbrix is the combination of Dalvo (my surname) and legacy.
We drive or support sales expansion. We also invest in promising companies and business operations with advisory and-or capital.
Our approach with our clients is tailor made, we leverage our expertise in Marketing, sales and our network to build a profitable sales expansion/presence.
The website needs to showcase the work we have done and it has to be easily updatable from a non-coder. The call to action is just one "contact us". I expect to connect a simple typeform after the CTA, and receive an email to our main email address.
I create a Team for every project/client. Lumbrix don't have employees, we gather the best people in my network to do the work. So our Team can go to 1 man band to 15+ people max.
In the Team I create I'll select Vibrant, very pro-active and energetic people, all with international experiences and track record.

I don't have a specific palette in mind, so feel free to create.

```html
<!DOCTYPE html>
<html lang="en">
<head>
<meta charset="utf-8">
<title>Lumbrix Ventures</title>
<link href="https://fonts.googleapis.com/css2?family=Poppins:wght@400;500;600;700&display=swap" rel="stylesheet">
<style>
:root{
  --teal:#4bbdab;
  --teal-light:#56c9b6;
  --teal-deep:#2f9d8d;
  --ink:#1b2b2f;
  --dark:#0e1c1e;
  --text:#2d3436;
  --muted:#6b7478;
  --card-head:#e9eef1;
  --white:#ffffff;
}
*{margin:0;padding:0;box-sizing:border-box}
html,body{width:1200px;height:3330px;overflow:hidden}
body{font-family:'Poppins',sans-serif;color:var(--text);background:var(--white);position:relative}
.abs{position:absolute}

/* header */
.site-header{position:absolute;top:0;left:0;width:1200px;height:86px;background:var(--white);z-index:3}
.brand-badge{position:absolute;left:111px;top:-40px;width:166px;height:206px;background:var(--white);border-radius:0 0 83px 83px;display:flex;flex-direction:column;align-items:center;justify-content:flex-end;padding-bottom:34px;z-index:4}
.brand-badge .dot{width:44px;height:44px;border-radius:50%;background:var(--teal);margin-bottom:12px}
.brand-badge .name{font-size:13px;font-weight:600;color:var(--ink)}
.main-nav{position:absolute;top:32px;left:555px;display:flex;gap:23px;font-size:15px;color:var(--ink)}
.main-nav .active{color:var(--teal)}
.btn{display:inline-flex;align-items:center;justify-content:center;font-size:15px;font-weight:500;color:var(--white);background:var(--ink);border-radius:18px 2px 18px 2px;position:absolute}
.btn-header{left:954px;top:22px;width:135px;height:40px}

/* hero */
.hero{position:absolute;top:86px;left:0;width:1200px;height:600px;background:linear-gradient(135deg,var(--teal-deep),var(--teal-light) 60%,var(--teal));border-radius:0 0 190px 0}
.hero-welcome{position:absolute;left:110px;top:214px;font-size:30px;font-weight:500;color:var(--white)}
.hero-title{position:absolute;left:106px;top:252px;font-size:60px;font-weight:700;color:var(--white);letter-spacing:-1px}
.btn-hero{left:110px;top:346px;width:133px;height:40px}
.hero-art{position:absolute;left:634px;top:130px;width:440px;height:400px;border-radius:24px;background:linear-gradient(160deg,rgba(255,255,255,.35),rgba(255,255,255,.12))}

/* section heads */
.section-title{position:absolute;left:0;width:1200px;text-align:center;font-size:46px;font-weight:700;color:var(--ink)}
.section-title.light{color:var(--white)}

/* about */
.about-col{position:absolute;top:830px;width:476px;font-size:16px;line-height:30px;text-align:justify;color:var(--text)}
.about-col strong{font-weight:500;color:var(--ink);display:block;text-align:left}
.btn-grad{background:linear-gradient(90deg,var(--teal-deep),var(--ink))}
.btn-learn{left:533px;top:1069px;width:133px;height:40px}

/* services */
.services{position:absolute;top:1162px;left:0;width:1200px;height:772px;background:var(--teal);border-radius:170px 0 170px 0}
.ring{position:absolute;left:0;top:0}
.svc-icon{position:absolute;width:96px;height:96px;border-radius:50%;background:radial-gradient(circle at 40% 35%,#3a5457,var(--ink));display:flex;align-items:center;justify-content:center}
.svc-title{position:absolute;font-size:22px;font-weight:500;color:var(--white)}
.svc-text{position:absolute;font-size:16px;line-height:28.5px;color:var(--white)}

/* works */
.work-card{position:absolute;top:2146px;width:467px;height:321px;background:var(--white);box-shadow:0 4px 18px rgba(0,0,0,.1)}
.work-head{height:139px;background:var(--card-head);padding:30px 31px 0}
.work-card.alt .work-head{background:#eaf2f9}
.work-head h3{font-size:21px;font-weight:500;line-height:29px;color:var(--ink)}
.work-head time{display:block;margin-top:12px;font-size:14px;color:var(--text)}
.work-body{padding:33px 31px 0;font-size:16px;line-height:28.5px;color:var(--text)}
.btn-view{left:533px;top:2519px;width:133px;height:40px}

/* contact band */
.touch{position:absolute;top:2617px;left:0;width:1200px;height:400px;background:var(--teal);border-radius:170px 0 0 0}
.touch-text{position:absolute;left:150px;top:2764px;width:900px;text-align:center;font-size:16px;line-height:29px;color:var(--white)}
.btn-touch{left:533px;top:2863px;width:133px;height:40px}

/* footer */
.site-footer{position:absolute;top:2967px;left:0;width:1200px;height:363px;background:var(--dark);border-radius:0 170px 0 0;color:var(--white)}
.foot-brand{position:absolute;left:114px;top:86px;display:flex;flex-direction:column;align-items:flex-start}
.foot-brand .dot{width:60px;height:60px;border-radius:50%;background:var(--white);margin-bottom:16px;margin-left:40px}
.foot-brand .name{font-size:16px;font-weight:600}
.foot-col{position:absolute;top:46px}
.foot-col h4{font-size:16px;font-weight:500;letter-spacing:1px;margin-bottom:18px}
.foot-col li{list-style:none;font-size:16px;height:30px;display:flex;align-items:center;gap:12px}
.chev{width:14px;height:12px}
.contact-row{display:flex;gap:24px;font-size:16px;line-height:30px;margin-bottom:12px}
.contact-row svg{flex:none;margin-top:7px}
.foot-rule{position:absolute;left:111px;top:295px;width:978px;height:1px;background:rgba(255,255,255,.3)}
.copyright{position:absolute;top:322px;left:0;width:1200px;text-align:center;font-size:16px}
</style>
</head>
<body>

<header class="site-header">
  <div class="brand-badge"><span class="dot"></span><span class="name">Lumbrix Ventures</span></div>
  <nav class="main-nav">
    <span class="active">Home</span><span>Our Services</span><span>About</span><span>Blog</span><span>Contact</span>
  </nav>
  <span class="btn btn-header">Get in touch</span>
</header>

<section class="hero">
  <p class="hero-welcome">Welcome To</p>
  <h1 class="hero-title">Lumbrix Ventures</h1>
  <span class="btn btn-hero">Contact Us</span>
  <div class="hero-art" role="img" aria-label="Illustration of an analytics dashboard with charts and app icons"></div>
</section>

<h2 class="section-title" style="top:742px">About Us</h2>
<p class="about-col" style="left:110px">Lorem ipsum dolor sit amet, consectetur adipiscing elit, sed do eiusmod tempor incididunt ut labore et dolore magna aliqua. Ut enim ad minim veniam, quis nostrud exercitation ullamco laboris nisi ut aliquip ex ea commodo consequat. Duis aute irure dolor in reprehenderit in voluptate velit esse cillum dolore eu fugiat nulla pariatur.</p>
<p class="about-col" style="left:614px">Lorem ipsum dolor sit amet, consectetur adipiscing elit, sed do eiusmod tempor incididunt ut labore et dolore magna aliqua. Ut enim ad minim veniam, quis nostrud exercitation ullamco laboris nisi ut aliquip ex ea commodo consequat. Eu fugiat nulla pariatur.<strong style="margin-top:3px">Excepteur sint occaecat cupidatat non proident, sunt in culpa qui offi cia deserunt.</strong></p>
<span class="btn btn-grad btn-learn">Learn More</span>

<section class="services">
  <h2 class="section-title light" style="top:82px">Our Services</h2>
  <svg class="ring" width="1200" height="772" aria-hidden="true">
    <circle cx="600" cy="370" r="168" fill="none" stroke="#bfe9e1" stroke-width="7"/>
  </svg>
  <div class="svc-icon" style="left:371px;top:277px">
    <svg width="48" height="48" viewBox="0 0 48 48" fill="none" stroke="#fff" stroke-width="2"><rect x="14" y="6" width="26" height="18" rx="2"/><path d="M24 11l8 4-8 4z"/><path d="M6 28l14-6v18L6 34z"/><path d="M10 35l3 9"/><path d="M26 28h8M26 33h6"/></svg>
  </div>
  <div class="svc-icon" style="left:732px;top:277px">
    <svg width="50" height="50" viewBox="0 0 50 50" fill="none" stroke="#fff" stroke-width="2"><circle cx="25" cy="25" r="14"/><path d="M11 25h28M25 11c-6 8-6 20 0 28M25 11c6 8 6 20 0 28"/><path d="M4 4l6 6M46 4l-6 6M4 46l6-6M46 46l-6-6"/></svg>
  </div>
  <div class="svc-icon" style="left:552px;top:473px">
    <svg width="50" height="50" viewBox="0 0 50 50" fill="none" stroke="#fff" stroke-width="2"><path d="M8 26l10-10 8 6 14-14"/><path d="M34 8h6v6"/><path d="M20 30v8M28 26v10M36 22v12"/><path d="M6 36l10 8h16l10-6"/></svg>
  </div>
  <h3 class="svc-title" style="right:850px;top:300px">Marketing</h3>
  <p class="svc-text" style="right:850px;top:334px;width:250px;text-align:right">Lorem ipsum dolor sit amet, consectetur adipiscing elit, sed eiusmod tempor incididun</p>
  <h3 class="svc-title" style="left:848px;top:300px">Expansion</h3>
  <p class="svc-text" style="left:850px;top:334px;width:250px">Lorem ipsum dolor sit amet, consectetur adipiscing elit, sed eiusmod tempor incididun</p>
  <h3 class="svc-title" style="left:0;width:1200px;text-align:center;top:584px">Sales</h3>
  <p class="svc-text" style="left:460px;width:280px;text-align:center;top:617px">Lorem ipsum dolor sit amet, consec tetur adipiscing elit, sed eiusmod tempor incididun</p>
</section>

<h2 class="section-title" style="top:2020px">Our Works</h2>
<article class="work-card" style="left:114px">
  <div class="work-head"><h3>Excepteur sint occaecat cupidatat non proident, sunt in</h3><time>29-12-2022</time></div>
  <p class="work-body">Sed ut perspiciatis unde omnis iste natus error sit voluptatem accusantium doloremqu laudantium, totam rem aperiam, eaque ipsa quae illinventore veritatis et quasi architecto beatae vitae.</p>
</article>
<article class="work-card alt" style="left:621px">
  <div class="work-head"><h3>Excepteur sint occaecat cupidatat non proident, sunt in</h3><time>29-12-2022</time></div>
  <p class="work-body">Sed ut perspiciatis unde omnis iste natus error sit voluptatem accusantium doloremqu laudantium, totam rem aperiam, eaque ipsa quae illinventore veritatis et quasi architecto beatae vitae.</p>
</article>
<span class="btn btn-view">View All</span>

<section class="touch"></section>
<h2 class="section-title light" style="top:2682px">Get In Touch</h2>
<p class="touch-text">Lorem ipsum dolor sit amet, consectetur adipiscing elit, sed do eiusmod tempor incididunt ut labore et dolore magna aliqua. Quis ipsum suspendisse ultrices gravida.</p>
<span class="btn btn-touch">Contact Us</span>

<footer class="site-footer">
  <div class="foot-brand"><span class="dot"></span><span class="name">Lumbrix Ventures</span></div>

  <div class="foot-col" style="left:375px">
    <h4>QUICK LINKS</h4>
    <ul>
      <li><svg class="chev" viewBox="0 0 14 12" fill="none" stroke="#4bbdab" stroke-width="1.6"><path d="M1 1l5 5-5 5M7 1l5 5-5 5"/></svg>Home</li>
      <li><svg class="chev" viewBox="0 0 14 12" fill="none" stroke="#4bbdab" stroke-width="1.6"><path d="M1 1l5 5-5 5M7 1l5 5-5 5"/></svg>About</li>
      <li><svg class="chev" viewBox="0 0 14 12" fill="none" stroke="#4bbdab" stroke-width="1.6"><path d="M1 1l5 5-5 5M7 1l5 5-5 5"/></svg>Services</li>
      <li><svg class="chev" viewBox="0 0 14 12" fill="none" stroke="#4bbdab" stroke-width="1.6"><path d="M1 1l5 5-5 5M7 1l5 5-5 5"/></svg>Blog</li>
      <li><svg class="chev" viewBox="0 0 14 12" fill="none" stroke="#4bbdab" stroke-width="1.6"><path d="M1 1l5 5-5 5M7 1l5 5-5 5"/></svg>Contact Us</li>
    </ul>
  </div>

  <div class="foot-col" style="left:596px">
    <h4>CONTACT</h4>
    <div class="contact-row"><svg width="16" height="20" viewBox="0 0 16 20"><path d="M8 0a8 8 0 018 8c0 6-8 12-8 12S0 14 0 8a8 8 0 018-8z" fill="#4bbdab"/><circle cx="8" cy="8" r="3" fill="#0e1c1e"/></svg><span>Lumbrix Ventures,<br>Address Comes Here.</span></div>
    <div class="contact-row"><svg width="16" height="16" viewBox="0 0 16 16"><path d="M3 1l3 3-2 2c1 2 3 4 5 5l2-2 3 3-2 3C7 15 1 9 0 3z" fill="#4bbdab"/></svg><span>+1555-014-227</span></div>
    <div class="contact-row"><svg width="16" height="16" viewBox="0 0 16 16" fill="#4bbdab"><rect x="4" y="0" width="8" height="4"/><rect x="0" y="5" width="16" height="7" rx="1"/><rect x="4" y="10" width="8" height="6"/></svg><span>info@lumbrixventures.com</span></div>
  </div>

  <div class="foot-col" style="left:912px">
    <h4>OTHER LINKS</h4>
    <ul>
      <li><svg class="chev" viewBox="0 0 14 12" fill="none" stroke="#4bbdab" stroke-width="1.6"><path d="M1 1l5 5-5 5M7 1l5 5-5 5"/></svg>Terms &amp; Condition</li>
      <li><svg class="chev" viewBox="0 0 14 12" fill="none" stroke="#4bbdab" stroke-width="1.6"><path d="M1 1l5 5-5 5M7 1l5 5-5 5"/></svg>Privacy Policy</li>
      <li><svg class="chev" viewBox="0 0 14 12" fill="none" stroke="#4bbdab" stroke-width="1.6"><path d="M1 1l5 5-5 5M7 1l5 5-5 5"/></svg>Cookies</li>
    </ul>
  </div>

  <div class="foot-rule"></div>
  <p class="copyright">2022 Lumbrix Ventures. All Rights Reserved.</p>
</footer>

</body>
</html>
```